Flooring Company Wordpress Design Using Elementor

We need a website design using elementor for a flooring company. I have attached a word document with the entire content for the site. I have sample websites www.pellingtonrenovatesutah.com and www.stonepathtilesdenver.com

The site needs to look alot better than the samples. Modern and professional is what we are looking for. 100 times better than the sample websites.

I have images to be used in the site but the file is to large to attached here.

```html
<!DOCTYPE html>
<html lang="en">
<head>
<meta charset="utf-8">
<title>Beacon Flooring Florida</title>
<link href="https://fonts.googleapis.com/css2?family=Montserrat:wght@500;600;700;800&family=Open+Sans:wght@400;600&display=swap" rel="stylesheet">
<style>
:root{
  --navy:#1f3a6b;
  --navy-dark:#162a4f;
  --orange:#f28a22;
  --ink:#2b2f36;
  --muted:#6c727c;
  --line:#e3e6eb;
  --soft:#f4f5f7;
  --footer:#1c1e23;
  --footer-bar:#141518;
  --white:#fff;
}
*{box-sizing:border-box;margin:0;padding:0}
html,body{width:1200px;height:3844px;overflow:hidden}
body{font-family:"Open Sans",Arial,sans-serif;color:var(--ink);background:var(--white);font-size:13px;line-height:1.6}
h1,h2,h3,h4,.btn,.nav a{font-family:"Montserrat",Arial,sans-serif}
section,footer{overflow:hidden}
.btn{display:inline-block;font-size:11px;font-weight:700;letter-spacing:.5px;padding:10px 22px;border-radius:22px;text-transform:uppercase;text-decoration:none}
.btn-orange{background:var(--orange);color:var(--white)}
.btn-outline{border:2px solid var(--white);color:var(--white)}
.btn-ghost{border:1px solid var(--line);color:var(--navy);padding:8px 16px;font-size:10px}
.btn-ghost-orange{border:1px solid var(--orange);color:var(--orange);padding:8px 16px;font-size:10px}

/* header */
.site-header{height:100px;display:flex;align-items:center;justify-content:space-between;padding:0 60px;background:var(--white);box-shadow:0 2px 8px rgba(0,0,0,.06);position:relative;z-index:2}
.brand{display:flex;align-items:center;gap:10px}
.brand-mark{width:30px;height:30px;background:var(--orange)}
.brand-name{font-family:"Montserrat",sans-serif;font-weight:800;font-size:22px;color:var(--navy);letter-spacing:.5px}
.nav{display:flex;gap:34px}
.nav a{font-size:12px;font-weight:600;color:var(--navy);text-decoration:none;padding:8px 0}
.nav a.active{color:var(--orange);border-bottom:2px solid var(--orange)}
.header-contact{text-align:right;font-size:12px;color:var(--navy);font-weight:600}
.header-contact .phone{display:flex;align-items:center;gap:6px;justify-content:flex-end}
.social{display:flex;gap:6px;justify-content:flex-end;margin-top:6px}
.social span{width:20px;height:20px;border-radius:50%;background:var(--orange);display:block}

/* hero */
.hero{height:460px;position:relative;background:linear-gradient(100deg,#3a3c40 0%,#6b6258 45%,#9c8468 70%,#5a5048 100%);color:var(--white);text-align:center;padding-top:80px}
.hero::after{content:"";position:absolute;inset:0;background:rgba(15,22,40,.35)}
.hero-inner{position:relative;z-index:1;width:960px;margin:0 auto}
.hero h1{font-size:34px;font-weight:800;line-height:1.25;text-transform:uppercase}
.hero p{font-size:14px;margin:22px auto 30px;width:660px;opacity:.95}
.hero .btns{display:flex;gap:16px;justify-content:center}

/* features */
.features{height:430px;padding:0 80px;position:relative;overflow:visible}
.feature-row{display:flex;gap:50px;margin-top:-30px;position:relative;z-index:1}
.feature{flex:1}
.feature-icon{width:84px;height:84px;background:var(--navy);display:flex;align-items:center;justify-content:center;margin-bottom:26px}
.feature:nth-child(2) .feature-icon{background:var(--orange)}
.feature h3{font-size:19px;color:var(--navy);font-weight:700;margin-bottom:12px}
.feature p{color:var(--muted);font-size:13px}
.features .cta{text-align:center;margin-top:34px}

/* partner */
.partner{height:400px;background:var(--soft);display:flex;align-items:center;padding:0 80px;gap:50px;overflow:visible}
.partner-text{width:460px}
.partner h2{font-size:26px;color:var(--navy);font-weight:800;border-left:5px solid var(--orange);padding-left:14px;line-height:1.2}
.partner h4{font-size:12px;color:var(--orange);margin:14px 0 12px;text-transform:uppercase}
.partner p{color:var(--muted);margin-bottom:10px}
.partner-photo{flex:1;height:300px;background:linear-gradient(135deg,#cfc7bc,#a89783 55%,#7d6a57);box-shadow:18px 18px 0 var(--navy)}

/* services */
.services{height:1020px;padding:60px 80px 0}
.section-title{display:flex;align-items:center;justify-content:center;gap:20px;text-align:center}
.section-title::before,.section-title::after{content:"";height:2px;width:120px;background:var(--orange)}
.section-title h2{font-size:26px;font-weight:800;color:var(--navy);text-transform:uppercase;line-height:1.25}
.card-grid{display:grid;grid-template-columns:repeat(3,1fr);gap:30px;margin-top:40px}
.card{background:var(--white);box-shadow:0 4px 16px rgba(0,0,0,.08)}
.card-photo{height:210px;position:relative}
.card-label{position:absolute;left:0;bottom:0;background:var(--navy);color:var(--white);font-family:"Montserrat",sans-serif;font-weight:700;font-size:12px;padding:8px 14px;text-transform:uppercase}
.card:nth-child(2) .card-label,.card:nth-child(6) .card-label{background:var(--orange)}
.card-body{padding:14px 18px 18px}
.card-body p{font-size:12px;color:var(--muted);margin-bottom:14px;min-height:76px}
.card-body .btns{display:flex;gap:10px}

/* testimonials */
.testimonials{height:440px;background:linear-gradient(180deg,#eef0f3,#f7f7f8);text-align:center;padding-top:40px;position:relative}
.avatar{width:70px;height:70px;border-radius:50%;background:linear-gradient(135deg,#c9cdd4,#8d95a1);margin:30px auto 20px;border:4px solid var(--white)}
.testimonials blockquote{width:720px;margin:0 auto;color:var(--muted);font-size:14px;font-style:italic}
.testimonials .who{margin:16px 0 22px;font-weight:600;color:var(--navy);font-size:13px}
.arrow{position:absolute;top:210px;width:36px;height:36px;border-radius:50%;border:1px solid #c6cbd3;display:flex;align-items:center;justify-content:center}
.arrow.prev{left:180px}.arrow.next{right:180px}

/* process */
.process{height:500px;padding-top:50px}
.steps{display:flex;justify-content:space-between;padding:0 100px;margin-top:44px;position:relative}
.steps::before{content:"";position:absolute;top:44px;left:220px;right:220px;border-top:2px dashed #c9ced6}
.step{width:220px;text-align:center;position:relative}
.step-icon{width:90px;height:90px;border-radius:50%;background:var(--white);border:2px solid var(--navy);margin:0 auto 20px;display:flex;align-items:center;justify-content:center}
.step:nth-child(2) .step-icon,.step:nth-child(4) .step-icon{border-color:var(--orange)}
.step h3{font-size:16px;font-weight:700;color:var(--navy);margin-bottom:10px}
.step:nth-child(2) h3,.step:nth-child(4) h3{color:var(--orange)}
.step p{font-size:12px;color:var(--muted)}

/* footer */
.site-footer{height:450px;background:var(--footer);color:#c7cad0;padding:60px 80px 0;display:flex;gap:80px}
.footer-info{width:420px}
.footer-info .brand-name{color:var(--white);font-size:20px}
.footer-info .row{display:flex;gap:10px;align-items:center;margin-top:16px;font-size:13px}
.footer-info .social{justify-content:flex-start;margin-top:24px;gap:10px}
.footer-info .social span{width:30px;height:30px}
.footer-form{flex:1}
.footer-form h3{color:var(--white);font-size:16px;font-weight:700;margin-bottom:20px;text-transform:uppercase}
.fields{display:grid;grid-template-columns:1fr 1fr;gap:12px}
.field{height:40px;background:#2a2d33;border:1px solid #3a3e46;color:#8b9099;font-size:12px;padding:10px 12px}
.field.wide{grid-column:span 2;height:90px}
.footer-form .btn{margin-top:16px}
.footer-bar{height:44px;background:var(--footer-bar);color:#8b9099;font-size:11px;display:flex;align-items:center;padding:0 80px}
</style>
</head>
<body>

<header class="site-header">
  <div class="brand"><span class="brand-mark"></span><span class="brand-name">BEACON FLOORING</span></div>
  <nav class="nav">
    <a class="active" href="#">HOME</a><a href="#">ABOUT US</a><a href="#">SERVICES</a><a href="#">FAQ</a><a href="#">TESTIMONIALS</a><a href="#">CONTACT US</a>
  </nav>
  <div class="header-contact">
    <div class="phone"><svg width="14" height="14" viewBox="0 0 24 24"><path fill="#f28a22" d="M6.6 10.8a15 15 0 0 0 6.6 6.6l2.2-2.2c.3-.3.7-.4 1-.2 1.1.4 2.3.6 3.6.6.6 0 1 .4 1 1V20c0 .6-.4 1-1 1A17 17 0 0 1 3 4c0-.6.4-1 1-1h3.5c.6 0 1 .4 1 1 0 1.3.2 2.5.6 3.6.1.3 0 .7-.2 1z"/></svg>+123-456-7890</div>
    <div class="social"><span></span><span></span></div>
  </div>
</header>

<section class="hero" role="img" aria-label="Bright living room with wide hardwood flooring and large windows">
  <div class="hero-inner">
    <h1>Change Your Building Flooring Story<br>With Beacon Group</h1>
    <p>Get your dream flooring, from residential to commercial projects. Our crew delivers quality installations, honest pricing and lasting results, so your floors look great and stay that way for years ahead.</p>
    <div class="btns"><a class="btn btn-outline" href="#">Explore More</a><a class="btn btn-orange" href="#">Get Your Free Estimate</a></div>
  </div>
</section>

<section class="features">
  <div class="feature-row">
    <div class="feature">
      <div class="feature-icon"><svg width="40" height="40" viewBox="0 0 40 40" fill="none" stroke="#fff" stroke-width="2"><rect x="4" y="4" width="14" height="14"/><rect x="22" y="4" width="14" height="14"/><rect x="4" y="22" width="14" height="14"/><rect x="22" y="22" width="14" height="14"/></svg></div>
      <h3>Minimal Stress on Your Plate</h3>
      <p>Floor installation or removal can be stressful for both parties. We move in, take care of every step and leave your property clean. Our team plans ahead, keeps you informed and finishes on schedule, so you can enjoy your new floors without any hassle from day one.</p>
    </div>
    <div class="feature">
      <div class="feature-icon"><svg width="40" height="40" viewBox="0 0 40 40" fill="none" stroke="#fff" stroke-width="2"><path d="M5 19 20 6l15 13"/><path d="M10 16v18h20V16"/><rect x="17" y="23" width="6" height="11"/></svg></div>
      <h3>A Finish Worthy of Your Home</h3>
      <p>The quality and type of your floor can do a lot for its style and value. The wrong installation could cost you more over time. We help you choose materials that suit your home, your budget and your daily life, then install them with care and precision.</p>
    </div>
    <div class="feature">
      <div class="feature-icon"><svg width="40" height="40" viewBox="0 0 40 40" fill="none" stroke="#fff" stroke-width="2"><circle cx="20" cy="16" r="10"/><path d="m15 16 4 4 7-7"/><path d="M13 25 10 36l10-5 10 5-3-11"/></svg></div>
      <h3>Qualified and Certified Experts</h3>
      <p>After spending years in flooring we know what it takes to do the job right. Every installer on our team is trained, certified and insured. We treat each space as our own and stand behind every floor we lay with a written workmanship guarantee.</p>
    </div>
  </div>
  <div class="cta"><a class="btn btn-ghost" href="#">Backed by Your Local Expert</a></div>
</section>

<section class="partner">
  <div class="partner-text">
    <h2>A RELIABLE PARTNER<br>TO LEAN ON</h2>
    <h4>Beacon Group comes with over 15 years of experience in floor installation</h4>
    <p>We are specialists when it comes to tile installation, hardwood installation, carpet installation, vinyl installation, laminate installation and floor removal. Over the years, we have served homeowners and businesses across the region.</p>
    <p>Our professional crews are customer-rated for all floor installation and removal needs. With us, you can expect on-time performance, professional service and complete craftsmanship.</p>
    <a class="btn btn-orange" href="#" style="margin-top:8px">Learn More</a>
  </div>
  <div class="partner-photo" role="img" aria-label="Modern living room with light wood flooring and a blue sofa"></div>
</section>

<section class="services">
  <div class="section-title"><h2>Make Your Floors Scream<br>Quality and Beauty</h2></div>
  <div class="card-grid">
    <article class="card">
      <div class="card-photo" role="img" aria-label="Installer laying large format floor tiles" style="background:linear-gradient(135deg,#b9a48e,#7c6a58)"><span class="card-label">Tile Installation</span></div>
      <div class="card-body"><p>Tile is one of the top flooring choices thanks to its durability and easy care. From porcelain to natural stone, we install every tile with level lines and clean grout.</p><div class="btns"><a class="btn btn-ghost" href="#">Learn More</a><a class="btn btn-ghost-orange" href="#">Get a Free Quote</a></div></div>
    </article>
    <article class="card">
      <div class="card-photo" role="img" aria-label="Hands fitting hardwood floor planks" style="background:linear-gradient(135deg,#c08a57,#6e4527)"><span class="card-label">Hardwood Installation</span></div>
      <div class="card-body"><p>Are you looking for hardwood that lasts for generations? We help you pick the right species and finish, then install solid or engineered boards to exact standards.</p><div class="btns"><a class="btn btn-ghost" href="#">Learn More</a><a class="btn btn-ghost-orange" href="#">Get a Free Quote</a></div></div>
    </article>
    <article class="card">
      <div class="card-photo" role="img" aria-label="Laminate planks being clicked into place" style="background:linear-gradient(135deg,#d2b995,#8e7455)"><span class="card-label">Laminate Installation</span></div>
      <div class="card-body"><p>Laminate offers a great look with budget-friendly pricing. It resists scratches and moisture, making it ideal for busy homes, rentals and active families with pets.</p><div class="btns"><a class="btn btn-ghost" href="#">Learn More</a><a class="btn btn-ghost-orange" href="#">Get a Free Quote</a></div></div>
    </article>
    <article class="card">
      <div class="card-photo" role="img" aria-label="Carpet being stretched across a room" style="background:linear-gradient(135deg,#a9b1bb,#5f6874)"><span class="card-label">Carpet Installation</span></div>
      <div class="card-body"><p>Carpet brings warmth and comfort to bedrooms and family rooms. We measure carefully, stretch properly and seam cleanly for a soft floor that wears evenly.</p><div class="btns"><a class="btn btn-ghost" href="#">Learn More</a><a class="btn btn-ghost-orange" href="#">Get a Free Quote</a></div></div>
    </article>
    <article class="card">
      <div class="card-photo" role="img" aria-label="Vinyl plank flooring samples" style="background:linear-gradient(135deg,#cdb08a,#9a7a55)"><span class="card-label">Vinyl Installation</span></div>
      <div class="card-body"><p>Vinyl is a popular option for kitchens and bathrooms, looking like wood or stone while staying waterproof. We install sheet and luxury plank vinyl with care.</p><div class="btns"><a class="btn btn-ghost" href="#">Learn More</a><a class="btn btn-ghost-orange" href="#">Get a Free Quote</a></div></div>
    </article>
    <article class="card">
      <div class="card-photo" role="img" aria-label="Old flooring being removed from a room" style="background:linear-gradient(135deg,#b7aa9b,#6f6357)"><span class="card-label">Floor Removal</span></div>
      <div class="card-body"><p>Replacing your old floors? We remove tile, wood, carpet and vinyl quickly, haul away debris and prepare the subfloor so your new installation starts on solid ground.</p><div class="btns"><a class="btn btn-ghost" href="#">Learn More</a><a class="btn btn-ghost-orange" href="#">Get a Free Quote</a></div></div>
    </article>
  </div>
</section>

<section class="testimonials">
  <div class="section-title"><h2>What Our Clients Say</h2></div>
  <div class="avatar" role="img" aria-label="Client portrait placeholder"></div>
  <span class="arrow prev"><svg width="12" height="12" viewBox="0 0 12 12"><path d="M8 1 3 6l5 5" fill="none" stroke="#1f3a6b" stroke-width="2"/></svg></span>
  <span class="arrow next"><svg width="12" height="12" viewBox="0 0 12 12"><path d="m4 1 5 5-5 5" fill="none" stroke="#1f3a6b" stroke-width="2"/></svg></span>
  <blockquote>"The crew arrived on time, explained every step and finished our whole first floor in just three days. The new hardwood looks stunning, the house was left spotless and the price matched the estimate exactly. We would gladly hire them again."</blockquote>
  <div class="who">Renee Calloway | Happy Customer</div>
  <a class="btn btn-orange" href="#">Learn More</a>
</section>

<section class="process">
  <div class="section-title"><h2>A Simple, Repeatable Process</h2></div>
  <div class="steps">
    <div class="step">
      <div class="step-icon"><svg width="36" height="36" viewBox="0 0 36 36" fill="none" stroke="#1f3a6b" stroke-width="2"><rect x="4" y="7" width="28" height="25" rx="2"/><path d="M4 14h28M11 3v7M25 3v7"/></svg></div>
      <h3>Schedule An Appointment</h3>
      <p>Fill out the form on our site or call us to book a visit. We measure your space, talk through your goals and give a clear estimate.</p>
    </div>
    <div class="step">
      <div class="step-icon"><svg width="36" height="36" viewBox="0 0 36 36" fill="none" stroke="#f28a22" stroke-width="2"><rect x="4" y="4" width="28" height="28"/><path d="M4 13h28M4 22h28M14 4v9M24 13v9M14 22v10"/></svg></div>
      <h3>Your Preferred Floor Material</h3>
      <p>Based on our findings we recommend the best options. We help you choose a material that fits your style, budget and daily use.</p>
    </div>
    <div class="step">
      <div class="step-icon"><svg width="36" height="36" viewBox="0 0 36 36" fill="none" stroke="#1f3a6b" stroke-width="2"><path d="M6 30 20 16"/><path d="m17 9 8-5 7 7-5 8-4-4-4 4-4-4 4-4z"/></svg></div>
      <h3>Premium Installation</h3>
      <p>Once the plan is approved our certified team installs your new floor with precision, respect for your home and a tidy finish.</p>
    </div>
    <div class="step">
      <div class="step-icon"><svg width="36" height="36" viewBox="0 0 36 36" fill="none" stroke="#f28a22" stroke-width="2"><circle cx="18" cy="18" r="14"/><path d="M12 21c1.5 3 4 4 6 4s4.5-1 6-4"/><circle cx="13" cy="14" r="1" fill="#f28a22"/><circle cx="23" cy="14" r="1" fill="#f28a22"/></svg></div>
      <h3>A Happy You!</h3>
      <p>With a final walkthrough we make sure you love the result. Enjoy your beautiful floors backed by our care tips and warranty.</p>
    </div>
  </div>
</section>

<footer class="site-footer">
  <div class="footer-info">
    <div class="brand"><span class="brand-mark"></span><span class="brand-name">BEACON FLOORING</span></div>
    <div class="row"><svg width="16" height="16" viewBox="0 0 24 24"><path fill="#f28a22" d="M6.6 10.8a15 15 0 0 0 6.6 6.6l2.2-2.2c.3-.3.7-.4 1-.2 1.1.4 2.3.6 3.6.6.6 0 1 .4 1 1V20c0 .6-.4 1-1 1A17 17 0 0 1 3 4c0-.6.4-1 1-1h3.5c.6 0 1 .4 1 1 0 1.3.2 2.5.6 3.6.1.3 0 .7-.2 1z"/></svg>+123-456-7890</div>
    <div class="row"><svg width="16" height="16" viewBox="0 0 24 24" fill="none" stroke="#f28a22" stroke-width="2"><rect x="3" y="5" width="18" height="14"/><path d="m3 6 9 7 9-7"/></svg>hello@beaconflooringfl.com</div>
    <div class="row"><svg width="16" height="16" viewBox="0 0 24 24"><path fill="#f28a22" d="M12 2a7 7 0 0 0-7 7c0 5 7 13 7 13s7-8 7-13a7 7 0 0 0-7-7zm0 9.5A2.5 2.5 0 1 1 12 6.5a2.5 2.5 0 0 1 0 5z"/></svg>482 Harbor View Lane, Coral Bay, FL 33012</div>
    <div class="social"><span></span><span></span><span></span></div>
  </div>
  <div class="footer-form">
    <h3>Get Started Now</h3>
    <div class="fields">
      <div class="field">Type of Flooring</div>
      <div class="field">Full Name</div>
      <div class="field">Email Address</div>
      <div class="field">Phone Number</div>
      <div class="field wide">Tell us about your project</div>
    </div>
    <a class="btn btn-orange" href="#">Submit</a>
  </div>
</footer>
<div class="footer-bar">© 2020 Beacon Flooring Florida. All Rights Reserved.</div>

</body>
</html>
```